Lumora Assist overview brochure

Take the word document that is attached and turn it into a brochure. (Thinking one page, front and back.) the only existing branding/colors we have is the logo that is on the document. It may require a phone all or a bit of back and forth in text to explain some of the concepts in the attached document.

Target Market(s)

Call centers

Industry/Entity Type

It Service

Font styles to use
Sans Serif

Colors

Designer to choose colors to be used in the design.

Requirements
Must have
• A crisp professional look

```html
<!DOCTYPE html>
<html lang="en">
<head>
<meta charset="utf-8">
<title>Lumora Assist – Overview Brochure</title>
<link href="https://fonts.googleapis.com/css2?family=Roboto+Condensed:wght@400;700&family=Open+Sans:wght@400;600;700&display=swap" rel="stylesheet">
<style>
  :root{
    --backdrop:#2e2926;
    --paper:#ffffff;
    --paper-warm:#f1efea;
    --brand-blue:#29a8e0;
    --brand-deep:#1d5f86;
    --brand-sky:#2fa9e1;
    --ink:#222222;
    --ink-soft:#444444;
    --slate:#5a5a5a;
    --bar-gray:#e6e6e6;
    --channel-green:#3bb54a;
    --white:#ffffff;
  }
  *{box-sizing:border-box;margin:0;padding:0}
  html,body{width:1200px;height:796px;overflow:hidden}
  body{background:var(--backdrop);position:relative;font-family:"Open Sans",Arial,sans-serif;color:var(--ink)}
  .page{position:absolute;top:56px;width:530px;height:684px;background:var(--paper);overflow:hidden}
  .page--front{left:58px;background:linear-gradient(180deg,#fff 0%,#fff 55%,var(--paper-warm) 75%,#fff 100%)}
  .page--back{left:614px}

  /* front */
  .brand-mark{position:absolute;left:38px;top:36px;display:flex;align-items:center;gap:14px}
  .brand-mark__dot{width:58px;height:58px;border-radius:50%;background:var(--brand-blue)}
  .brand-mark__name{font-family:"Roboto Condensed",Arial,sans-serif;font-weight:700;font-size:44px;line-height:1;color:var(--brand-deep)}
  .hero{position:absolute;left:0;top:0;width:530px;height:440px}
  .badge{position:absolute;left:330px;top:220px;width:148px;height:148px;border-radius:50%;
    background:radial-gradient(circle at 50% 40%,#6a6a6a,#3a3a3a 75%);border:6px solid #e8e8e8;
    box-shadow:0 3px 6px rgba(0,0,0,.35);display:flex;flex-direction:column;align-items:center;justify-content:center;
    font-family:"Roboto Condensed",Arial,sans-serif;font-weight:700;color:var(--white);text-align:center;line-height:1.08}
  .badge__big{font-size:27px}
  .badge__small{font-size:21px}
  .headline{position:absolute;left:30px;top:384px;width:470px;font-family:"Roboto Condensed",Arial,sans-serif;font-weight:700;font-size:20.5px;line-height:24px;color:var(--brand-deep)}
  .body-cols{position:absolute;left:30px;top:472px;width:468px;display:grid;grid-template-columns:215px 215px;column-gap:38px;font-size:7.1px;line-height:11.6px;color:var(--ink-soft);text-align:justify}
  .body-cols p{margin-bottom:7px}
  .body-cols__divider{position:absolute;left:234px;top:0;width:1px;height:116px;background:#cfcfcf}
  .front-foot__lead{position:absolute;left:28px;top:608px;font-family:"Roboto Condensed",Arial,sans-serif;font-weight:700;font-size:21px;color:var(--brand-sky)}
  .front-foot__url{position:absolute;left:28px;top:640px;font-weight:700;font-size:14.5px;letter-spacing:.6px;color:var(--ink)}
  .front-foot__contact{position:absolute;right:30px;top:604px;text-align:right;font-family:"Roboto Condensed",Arial,sans-serif}
  .front-foot__label{font-size:19px;color:var(--ink)}
  .front-foot__phone{font-weight:700;font-size:23px;color:var(--brand-sky)}

  /* back */
  .cost-list{position:absolute;left:34px;top:38px;width:272px}
  .cost-row{display:flex;height:42px;margin-bottom:7px;box-shadow:0 2px 3px rgba(0,0,0,.25)}
  .cost-row__icon{width:62px;background:linear-gradient(180deg,#f4f4f4,#cfcfcf);display:flex;align-items:center;justify-content:center}
  .cost-row__text{flex:1;background:var(--brand-sky);color:var(--white);font-weight:600;font-size:11.5px;line-height:16px;padding:4px 10px}
  .cost-note{position:absolute;left:68px;top:184px;font-size:8px;color:var(--ink-soft)}
  .contact-bar{position:absolute;left:38px;top:210px;width:268px;height:24px;background:var(--bar-gray);font-family:"Roboto Condensed",Arial,sans-serif;font-size:19px;line-height:24px;text-align:center;color:var(--ink)}
  .contact-bar strong{font-weight:700}
  .back-mark{position:absolute;left:80px;top:250px;display:flex;align-items:center;gap:10px}
  .back-mark__dot{width:40px;height:40px;border-radius:50%;background:var(--brand-blue)}
  .back-mark__name{font-family:"Roboto Condensed",Arial,sans-serif;font-weight:700;font-size:27px;color:var(--brand-deep)}
  .channels{position:absolute;left:330px;top:30px;width:174px;display:grid;grid-template-columns:repeat(3,58px);row-gap:4px}
  .channel{display:flex;flex-direction:column;align-items:center;gap:3px;height:46px}
  .channel__dot{width:32px;height:32px;border-radius:50%;background:var(--brand-blue)}
  .channel__dot--green{background:var(--channel-green)}
  .channel__name{font-weight:700;font-size:8px;line-height:11px;color:var(--slate)}
  .channel-copy{position:absolute;right:31px;top:155px;text-align:right;font-weight:700;font-size:13.5px;line-height:23px;color:#333;white-space:nowrap}
  .model-bar{position:absolute;left:0;top:304px;width:530px;height:28px;background:linear-gradient(180deg,#3c3c3c,#6a6a6a);color:var(--white);font-family:"Roboto Condensed",Arial,sans-serif;font-weight:700;font-size:21px;line-height:28px;text-align:center;letter-spacing:.5px}
  .model-panel{position:absolute;left:0;top:332px;width:530px;height:352px;background:var(--brand-sky);color:#10222e}
  .proposal{position:absolute;left:29px;top:22px;width:470px;font-size:9px;line-height:12px}
  .proposal__title{font-weight:700;font-size:17px;color:#111}
  .proposal__lead{font-size:11px}
  .proposal-rule{position:absolute;left:29px;top:56px;width:432px;height:1px;background:rgba(255,255,255,.7)}
  .col{position:absolute;top:76px;width:228px}
  .col--left{left:29px}
  .col--right{left:309px;width:200px}
  .col__title{font-weight:700;font-size:16.5px;color:#111;margin-bottom:10px}
  .col__intro{font-weight:600;font-size:11px;line-height:13px;color:#111;margin-bottom:12px}
  .col ul{list-style:none}
  .col li{position:relative;padding-left:13px;font-size:9.4px;line-height:12.4px;color:var(--white);margin-bottom:4px}
  .col li::before{content:"";position:absolute;left:0;top:3px;width:6px;height:6px;border-radius:50%;border:1.5px solid var(--white)}
  .col-divider{position:absolute;left:277px;top:82px;width:1px;height:250px;background:rgba(255,255,255,.6)}
</style>
</head>
<body>

<section class="page page--front">
  <svg class="hero" viewBox="0 0 530 440">
    <defs>
      <clipPath id="heroClip">
        <path d="M0 150 L430 120 Q470 180 480 250 Q470 330 400 352 Q250 380 120 360 Q50 348 0 340 Z"/>
      </clipPath>
      <linearGradient id="heroFill" x1="0" y1="0" x2="1" y2="1">
        <stop offset="0" stop-color="#dfe6ea"/>
        <stop offset=".5" stop-color="#b9c3c9"/>
        <stop offset="1" stop-color="#8a949a"/>
      </linearGradient>
    </defs>
    <path d="M440 0 L530 0 L530 330 Q515 260 490 180 Q470 90 440 0 Z" fill="#4a4a4a"/>
    <path d="M400 0 L470 0 Q510 110 510 240 Q505 330 440 370 Q480 300 478 220 Q470 100 400 0 Z" fill="var(--brand-blue)"/>
    <path d="M0 345 Q60 372 140 380 Q280 392 400 350 Q330 395 170 394 Q70 390 0 365 Z" fill="var(--brand-blue)"/>
    <g clip-path="url(#heroClip)">
      <rect role="img" aria-label="Photo of smiling contact-centre agents wearing headsets at computer workstations" x="0" y="110" width="490" height="280" fill="url(#heroFill)"/>
    </g>
  </svg>

  <div class="brand-mark">
    <span class="brand-mark__dot"></span>
    <span class="brand-mark__name">Lumora Assist</span>
  </div>

  <div class="badge">
    <span class="badge__big">100%</span>
    <span class="badge__small">Customer</span>
    <span class="badge__small">Satisfaction</span>
  </div>

  <h1 class="headline">Lumora Assist helps contact centers serve new customer access channels, improve customer service, and lower costs of operation.</h1>

  <div class="body-cols">
    <div>
      <p>The huge popularity of social media and messaging is creating customer preferences to communicate with your company using SMS text messaging, Friendbook Messenger, Threadly, Vira, Echovox, Homenest, and many other new channels.</p>
      <p>App fatigue has set in. Customers are weary of installing, updating and learning how to use mobile apps. Your customers want to communicate with you using their messaging service of choice or just talk into their smart phone, computer, Echovox or similar device.</p>
    </div>
    <div>
      <p>Sensible automation of customer interactions on these new channels can provide better service at even lower costs of operation.</p>
      <p>According to Garrison Research's report, by 2020, 85% of customer interactions will be managed without a human.</p>
      <p>Using specific techniques, Lumora Assist will help you shift some traffic from higher cost telephone calls to lower cost messaging channels. Shaping your traffic into lower cost channels has great financial benefits.</p>
    </div>
    <span class="body-cols__divider"></span>
  </div>

  <p class="front-foot__lead">Existing channels have different costs</p>
  <p class="front-foot__url">www.LumoraSolutions.net</p>
  <div class="front-foot__contact">
    <p class="front-foot__label">Contact Us</p>
    <p class="front-foot__phone">555-014-2290</p>
  </div>
</section>

<section class="page page--back">
  <div class="cost-list">
    <div class="cost-row">
      <div class="cost-row__icon">
        <svg width="30" height="30" viewBox="0 0 24 24"><path d="M6.6 10.8a15 15 0 006.6 6.6l2.2-2.2a1 1 0 011-.25 11 11 0 003.6.6 1 1 0 011 1V20a1 1 0 01-1 1A17 17 0 013 4a1 1 0 011-1h3.5a1 1 0 011 1 11 11 0 00.6 3.6 1 1 0 01-.25 1z" fill="#1d5f86"/></svg>
      </div>
      <div class="cost-row__text">Telephone call with a live agent<br>Average cost per call is $17 *</div>
    </div>
    <div class="cost-row">
      <div class="cost-row__icon">
        <svg width="32" height="24" viewBox="0 0 32 24"><rect x="1" y="2" width="30" height="20" rx="2" fill="#fff" stroke="#1d5f86" stroke-width="2"/><path d="M2 4 L16 14 L30 4" fill="none" stroke="#1d5f86" stroke-width="2"/></svg>
      </div>
      <div class="cost-row__text">Email with a live agent<br>Average cost per email is $15*</div>
    </div>
    <div class="cost-row">
      <div class="cost-row__icon">
        <svg width="38" height="32" viewBox="0 0 38 32"><path d="M2 2h34v20H13l-7 7v-7H2z" fill="#1d5f86"/><text x="19" y="10.5" font-family="Open Sans, sans-serif" font-size="6.5" font-weight="700" fill="#fff" text-anchor="middle">LIVE</text><text x="19" y="18" font-family="Open Sans, sans-serif" font-size="6.5" font-weight="700" fill="#fff" text-anchor="middle">CHAT</text></svg>
      </div>
      <div class="cost-row__text">Webchat with a live agent<br>Average cost per web chat is $12*</div>
    </div>
  </div>
  <p class="cost-note">*Above costs are sited from an HDX research paper</p>
  <div class="contact-bar">Contact Us: <strong>555-014-2290</strong></div>
  <div class="back-mark">
    <span class="back-mark__dot"></span>
    <span class="back-mark__name">Lumora Assist</span>
  </div>

  <div class="channels">
    <div class="channel"><span class="channel__dot"></span><span class="channel__name">SMS</span></div>
    <div class="channel"><span class="channel__dot"></span><span class="channel__name">Homenest</span></div>
    <div class="channel"><span class="channel__dot"></span><span class="channel__name">Echovox</span></div>
    <div class="channel"><span class="channel__dot channel__dot--green"></span><span class="channel__name">Kibo</span></div>
    <div class="channel"><span class="channel__dot"></span><span class="channel__name">Threadly</span></div>
    <div class="channel"><span class="channel__dot channel__dot--green"></span><span class="channel__name">Wavechat</span></div>
    <div class="channel"><span class="channel__dot channel__dot--green"></span><span class="channel__name">Pingapp</span></div>
  </div>
  <p class="channel-copy">With these new<br>channels, the cost<br>is similar to webchat.<br>Carefully automated<br>interactions are at an<br>even lower cost</p>

  <div class="model-bar">ENGAGEMENT MODEL</div>
  <div class="model-panel">
    <p class="proposal"><span class="proposal__title">Proposal:</span> <span class="proposal__lead">Lumora Assist provides a written proposal.</span> The proposal will describe our engagement methodologies and costs.</p>
    <span class="proposal-rule"></span>

    <div class="col col--left">
      <h2 class="col__title">Engagement</h2>
      <p class="col__intro">Lumora Assist will meet with all the relevant stake holders on site and gather information to identify:</p>
      <ul>
        <li>Historical traffic patterns.</li>
        <li>Actual costs by channel</li>
        <li>Review marketing plans that may impact customer service</li>
        <li>Review product plans that may impact customer service.</li>
        <li>Explore competition landscape as it relates to customer service.</li>
        <li>Review the existing corporate data store, analytics and reporting</li>
        <li>Review the current plans, metrics and budgets for customer service support</li>
      </ul>
    </div>
    <span class="col-divider"></span>
    <div class="col col--right">
      <h2 class="col__title">Transformation Report</h2>
      <ul>
        <li>Executive summary</li>
        <li>Cost analysis per contact by channel</li>
        <li>Traffic patterns by channel</li>
        <li>Probable impacts of product and marketing plans</li>
        <li>Recommendations for achieving competitive advantage through service</li>
        <li>Recommendations for new channel types</li>
        <li>Recommendations for traffic shaping</li>
        <li>Near and long-term options for sensible automation</li>
        <li>Technology recommendations for implementing new channels</li>
        <li>Projected financial impact of recommendations</li>
      </ul>
    </div>
  </div>
</section>

</body>
</html>
```